PDN Letterhead

We need a letterhead design that will be able to be used on all marketing products (letterhead, mail chimp, envelops, business cards, etc.) We are a law firm specializing primarily in transportation law but offer a wide range of services to our clients. We would like the design to be modern, simple, and professional. Our colors are black and gold, however, we've incorporated dark gray and white on other marketing products such as our website.

```html
<!DOCTYPE html>
<html lang="en">
<head>
<meta charset="utf-8">
<title>PDN Letterhead</title>
<link rel="stylesheet" href="https://fonts.googleapis.com/css2?family=Lato:ital,wght@0,400;0,700;1,400&display=swap">
<style>
  :root {
    --backdrop: #d3c7c5;
    --paper: #ffffff;
    --ink: #3b3b3b;
    --ink-soft: #6a6a6a;
    --black: #111111;
    --gold: #b39466;
    --stripe: #eeedea;
  }
  * { box-sizing: border-box; margin: 0; padding: 0; }
  html, body { width: 1200px; height: 784px; overflow: hidden; }
  body {
    background: var(--backdrop);
    font-family: "Lato", sans-serif;
    color: var(--ink);
    position: relative;
  }
  .letterhead {
    position: absolute;
    left: 320px; top: 30px;
    width: 560px; height: 724px;
    background: var(--paper);
    box-shadow: 0 6px 18px rgba(60, 40, 40, 0.18);
    overflow: hidden;
  }
  .brand {
    position: absolute;
    right: 46px; top: 44px;
    display: flex; align-items: center; gap: 8px;
    font-weight: 700; font-size: 22px; letter-spacing: 2px;
    color: var(--black);
    text-transform: uppercase;
  }
  .brand-mark {
    width: 12px; height: 12px; background: var(--gold);
  }
  .letter {
    position: absolute;
    left: 52px; right: 52px; top: 110px;
    font-size: 11.4px; line-height: 1.45; font-style: italic;
  }
  .letter .salutation { margin-bottom: 10px; }
  .letter p.body { text-indent: 26px; margin-bottom: 14px; }
  .signoff {
    position: absolute; left: 52px; top: 470px;
  }
  .signoff .regards {
    color: var(--gold); font-size: 12px; font-style: italic;
  }
  .signature {
    display: block; width: 120px; height: 34px; margin-top: 6px;
    background: linear-gradient(90deg, #f6f1e9, #efe5d4);
  }
  .contact {
    position: absolute; left: 52px; top: 540px;
    list-style: none;
    font-size: 10px; line-height: 1.55; color: var(--ink-soft); font-style: italic;
  }
  .contact li { display: flex; align-items: center; gap: 6px; }
  .contact .no-icon { padding-left: 16px; }
  .contact svg { width: 10px; height: 10px; flex: none; }
  .corner-decor {
    position: absolute; right: 0; bottom: 8px;
    width: 300px; height: 170px;
    background: linear-gradient(160deg, rgba(255,255,255,0) 10%, var(--stripe) 70%);
  }
  .footer-band {
    position: absolute; left: 0; right: 0; bottom: 0;
    height: 8px; display: flex;
  }
  .footer-band .band-black { width: 9%; background: var(--black); }
  .footer-band .band-gold { flex: 1; background: var(--gold); }
</style>
</head>
<body>
  <main class="letterhead">
    <header class="brand">
      <span class="brand-mark"></span>
      <span class="brand-name">PDN Law Group</span>
    </header>

    <section class="letter">
      <p class="salutation">Dear Sir/Mam,</p>
      <p class="body">Contrary to popular belief, Lorem Ipsum is not simply random text. It has roots in a piece of classical Latin literature from 45 BC, making it over 2000 years old. Daniel Hartwell, a Latin professor at Ashford Hill College in Virginia, looked up one of the more obscure Latin words, consectetur, from a Lorem Ipsum passage, and going through the cites of the word in classical literature, discovered the undoubtable source.</p>
      <p class="body">Lorem Ipsum comes from sections 1.10.32 and 1.10.33 of "de Finibus Bonorum et Malorum" (The Extremes of Good and Evil) by Lucius Corvan, written in 45 BC. This book is a treatise on the theory of ethics, very popular during the Renaissance. The first line of Lorem Ipsum, "Lorem ipsum dolor sit amet..", comes from a line in section 1.10.32.</p>
      <p class="body">The standard chunk of Lorem Ipsum used since the 1500s is reproduced below for those interested. Sections 1.10.32 and 1.10.33 from "de Finibus Bonorum et Malorum" by Lucius Corvan are also reproduced in their exact original form, accompanied by English versions from the 1914 translation by H. Pellmore.</p>
    </section>

    <section class="signoff">
      <p class="regards">Best Regards</p>
      <span class="signature" role="img" aria-label="Handwritten signature"></span>
    </section>

    <ul class="contact">
      <li><span class="no-icon">1234 First Line Address</span></li>
      <li><span class="no-icon">5678 Second Line Address</span></li>
      <li>
        <svg viewBox="0 0 10 10" aria-hidden="true"><path d="M2 1 L4 1 L4.6 3 L3.5 3.8 Q4.5 5.8 6.2 6.5 L7 5.4 L9 6 L9 8 Q5 9 2 5 Q1 3 2 1 Z" fill="#3b3b3b"/></svg>
        <span>(111) 999-0000</span>
      </li>
      <li>
        <svg viewBox="0 0 10 10" aria-hidden="true"><rect x="0.5" y="2" width="9" height="6" rx="1" fill="#3b3b3b"/><path d="M1 2.5 L5 5.5 L9 2.5" stroke="#fff" stroke-width="0.8" fill="none"/></svg>
        <span>info@yourmail.com</span>
      </li>
      <li>
        <svg viewBox="0 0 10 10" aria-hidden="true"><circle cx="5" cy="5" r="4.2" fill="none" stroke="#b39466" stroke-width="1"/><path d="M1 5 H9 M5 1 Q2.5 5 5 9 Q7.5 5 5 1" stroke="#b39466" stroke-width="0.7" fill="none"/></svg>
        <span>www.yourwebsite.com</span>
      </li>
    </ul>

    <div class="corner-decor" role="img" aria-label="Faint light grey diagonal decoration"></div>

    <div class="footer-band">
      <span class="band-black"></span>
      <span class="band-gold"></span>
    </div>
  </main>
</body>
</html>
```